coaching agenda

Please redesign the brochure attached in a more modern/trendy out look. I want something completely different to what is attached but using the same colours and logo.

```html
<!DOCTYPE html>
<html lang="en">
<head>
<meta charset="utf-8">
<title>Coaching Agenda – Make the uncommon common</title>
<link href="https://fonts.googleapis.com/css2?family=Ubuntu:wght@400;500;700&display=swap" rel="stylesheet">
<style>
  :root {
    --brand-blue: #14a9de;
    --badge-blue: #1f8fd0;
    --bullet-shadow: #0f5f96;
    --ink: #555a5f;
    --ink-strong: #4a4f54;
    --paper: #ffffff;
  }
  * { margin: 0; padding: 0; box-sizing: border-box; }
  html, body { width: 946px; height: 1200px; overflow: hidden; background: var(--paper); }
  body { font-family: "Ubuntu", sans-serif; color: var(--ink); }
  .page { position: relative; width: 946px; height: 1200px; background: var(--paper); }
  .band { position: absolute; left: 0; width: 100%; background: var(--brand-blue); }
  .band--top { top: 0; height: 26px; }
  .band--bottom { bottom: 0; height: 36px; }

  .section-badge { position: absolute; left: 68px; top: 99px; width: 67px; height: 52px; }
  .section-badge__num { position: absolute; left: 8px; top: 0; line-height: 52px; font-size: 27px; font-weight: 700; color: var(--paper); }
  .section-title { position: absolute; left: 161px; top: 112px; font-size: 23px; font-weight: 500; color: var(--ink-strong); line-height: 30px; }

  .item { position: absolute; left: 196px; width: 700px; font-size: 17px; line-height: 26px; }
  .item::before {
    content: ""; position: absolute; left: -47px; top: 8px; width: 10px; height: 10px;
    background: var(--brand-blue); box-shadow: 2px 2px 0 var(--bullet-shadow);
  }
  .item--plain::before { display: none; }
  .item--heading { font-weight: 700; color: var(--ink-strong); font-size: 18px; }
  .year { position: absolute; left: 321px; font-size: 17px; line-height: 26px; color: var(--brand-blue); }
  .domain { color: var(--brand-blue); font-weight: 700; font-size: 19px; }

  .brand-mark {
    position: absolute; left: 805px; top: 1119px; width: 64px; height: 64px; border-radius: 50%;
    background: var(--paper); border: 3px solid var(--brand-blue);
    display: flex; align-items: center; justify-content: center;
    font-size: 10px; font-weight: 500; color: var(--ink-strong); text-align: center; line-height: 12px;
  }
</style>
</head>
<body>
<main class="page">
  <div class="band band--top"></div>

  <svg class="section-badge" viewBox="0 0 67 52" aria-hidden="true">
    <path d="M4 0 H67 L52 26 L67 52 H4 Q0 52 0 48 V4 Q0 0 4 0 Z" fill="var(--badge-blue)"/>
  </svg>
  <div class="section-badge"><span class="section-badge__num">12</span></div>
  <h1 class="section-title">Make the uncommon common</h1>

  <p class="item" style="top:181px">Time – no time is no excuse – you cannot be defined by time in 2018/ the need to do more for less following the industry discounting of fees.</p>
  <p class="item" style="top:260px">How you manage free time</p>
  <p class="item" style="top:312px">You cannot be defined by not knowing what to do</p>
  <p class="item" style="top:365px">Embrace where your market is at:</p>
  <p class="year" style="top:397px">2015 – Wow</p>
  <p class="year" style="top:429px">2016 – Hope</p>
  <p class="year" style="top:461px">2017 – New norm</p>
  <p class="year" style="top:492px">2018 – The norm</p>

  <p class="item item--heading" style="top:530px">What are your behaviours costing you</p>
  <p class="item item--plain" style="top:566px"><span class="domain">Public domain</span> – those areas where people see you acting on your behaviours, both positive &amp; negative. Professionalism, application, integrity, self-esteem, respect for others &amp; proficiency are on display here</p>
  <p class="item item--plain" style="top:670px"><span class="domain">Private domain</span> – is the one where we spend time with ourselves &amp; where our mind games play out. This is the biggest behavioural game of all as we confront out habits, limitations, acceptance of disruptions, temptations &amp; fears</p>

  <p class="item" style="top:795px">Know your CRM system</p>
  <p class="item" style="top:833px">Capture data &amp; use it to generate an income</p>
  <p class="item" style="top:871px">Buyer work</p>
  <p class="item" style="top:908px">6 weeks after settlement</p>
  <p class="item" style="top:946px">Significantly increase the number of “just listed” you drop</p>
  <p class="item" style="top:984px">Put a name to a property</p>

  <div class="band band--bottom"></div>
  <div class="brand-mark">Rowan<br>Ellis</div>
</main>
</body>
</html>
```